Tidal Hounds Dog Behaviour, Training and Natural Healthcare Business Card Design

I am an experienced and qualified dog behavioural trainer and natural animal healthcare consultant offering a range of services to help pet dog owners with the "whole dog".
COLOURS: A soft light blue in the background - can be fading out or split, red should also feature
LOGO: Dog, healing hands, silhouette, shadow
SERVICES: Behaviour Consults, Training, Complex Skills Coaching Walking Coaching, Diet & Nutrition, Environmental Enrichment, Lifestyle and Lifestage Adaptations, Massage, Natural Health Options
BY LINE: Happy Dogs, Happy Owners
VALUES: Promoting communication and connection between dogs and their owners.
FOCUS: Nutritional guidance and environmental adaptation are often needed to complete the package and increase the success rate of training and behaviour modification.

Target Market(s)

Everyone who has a dog who they wish to improve their relationship with

Industry/Entity Type

Communication

Contact Information for Business Card

Tidal Hounds, Rosalind Vukovic, 0417 286350, tidalhounds7@quellmail.net, www.tidalhounds7.net, Qualified Dog Behavioural Trainer and Natural Animal Healthcare Consultant

Font styles to use
Sans Serif
Script

Colors
85cae6
ec2027

Requirements
Must have
• A clear indication that it is a dog services business. A raised feature
Should not have
• Pawprints, cartoons

Files

```html
<!DOCTYPE html>
<html lang="en">
<head>
<meta charset="utf-8">
<title>Tidal Hounds – Business Card</title>
<link rel="stylesheet" href="https://fonts.googleapis.com/css2?family=PT+Sans:wght@400;700&display=swap">
<style>
  :root {
    --page-bg: #2a2a2a;
    --band-black: #1d1d1d;
    --brand-blue: #85cae6;
    --brand-red: #e8232a;
    --photo-light: #e4e0d9;
    --photo-mid: #bdb5aa;
    --photo-dark: #8d8478;
    --text-white: #ffffff;
  }
  html, body {
    margin: 0;
    padding: 0;
    width: 1200px;
    height: 900px;
    overflow: hidden;
    background: var(--page-bg);
    font-family: "PT Sans", sans-serif;
  }
  .business-card {
    position: absolute;
    left: 100px;
    top: 150px;
    width: 1000px;
    height: 600px;
    overflow: hidden;
    box-shadow: 0 20px 50px rgba(0,0,0,0.5);
  }
  .card-art {
    position: absolute;
    inset: 0;
  }
  .brand-header {
    position: absolute;
    top: 0;
    left: 0;
    width: 1000px;
    height: 112px;
    text-align: center;
    color: var(--brand-blue);
  }
  .brand-name {
    position: absolute;
    left: 380px;
    top: 6px;
    margin: 0;
    font-size: 58px;
    font-weight: 400;
    letter-spacing: 2px;
    line-height: 1;
  }
  .brand-tagline {
    position: absolute;
    left: 200px;
    top: 64px;
    width: 720px;
    margin: 0;
    font-size: 19px;
    letter-spacing: 1.5px;
    line-height: 1.15;
  }
  .contact-person {
    position: absolute;
    left: 630px;
    top: 330px;
    color: var(--text-white);
  }
  .person-name {
    margin: 0;
    font-size: 40px;
    font-weight: 400;
    letter-spacing: 1px;
    line-height: 1.1;
  }
  .person-phone {
    margin: 0 0 0 14px;
    font-size: 28px;
    letter-spacing: 3px;
  }
  .contact-line {
    position: absolute;
    display: flex;
    align-items: center;
    gap: 14px;
    color: var(--text-white);
    font-size: 22px;
    letter-spacing: 1px;
  }
  .contact-email { left: 40px; top: 470px; }
  .contact-web { left: 390px; top: 530px; }
  .contact-icon { width: 22px; height: 22px; flex: none; }
</style>
</head>
<body>
  <div class="business-card">
    <svg class="card-art" width="1000" height="600" viewBox="0 0 1000 600">
      <defs>
        <linearGradient id="photoTone" x1="0" y1="0" x2="1" y2="1">
          <stop offset="0" stop-color="var(--photo-mid)"/>
          <stop offset="0.5" stop-color="var(--photo-light)"/>
          <stop offset="1" stop-color="var(--photo-dark)"/>
        </linearGradient>
      </defs>
      <rect class="dog-photo" x="0" y="100" width="1000" height="320" fill="url(#photoTone)" role="img" aria-label="Sepia photo of a happy white dog"/>
      <rect class="header-band" x="0" y="0" width="1000" height="112" fill="var(--band-black)"/>
      <path class="red-panel" d="M0,390 C330,392 640,300 790,112 L1000,112 L1000,600 L0,600 Z" fill="var(--brand-red)"/>
      <path class="blue-swoosh" d="M0,390 C330,392 640,300 790,112" fill="none" stroke="var(--brand-blue)" stroke-width="5"/>
      <path class="accent-line" d="M0,398 C420,390 720,250 1000,175" fill="none" stroke="var(--brand-blue)" stroke-width="1.2" opacity="0.8"/>
    </svg>

    <header class="brand-header">
      <h1 class="brand-name">Tidal Hounds</h1>
      <p class="brand-tagline">Qualified Dog Behavioural<br>Trainer and Natural Animal Healthcare Consultant</p>
    </header>

    <div class="contact-person">
      <p class="person-name">Rosalind Vukovic</p>
      <p class="person-phone">0417 286350</p>
    </div>

    <div class="contact-line contact-email">
      <svg class="contact-icon" viewBox="0 0 22 22">
        <circle cx="11" cy="11" r="10" fill="var(--text-white)"/>
        <rect x="5" y="7" width="12" height="8" fill="none" stroke="var(--brand-red)" stroke-width="1.5"/>
        <path d="M5,7 L11,12 L17,7" fill="none" stroke="var(--brand-red)" stroke-width="1.5"/>
      </svg>
      <span>tidalhounds7@quellmail.net</span>
    </div>

    <div class="contact-line contact-web">
      <svg class="contact-icon" viewBox="0 0 22 22">
        <circle cx="11" cy="11" r="10" fill="var(--text-white)"/>
        <circle cx="11" cy="11" r="6.5" fill="none" stroke="var(--brand-red)" stroke-width="1.3"/>
        <ellipse cx="11" cy="11" rx="3" ry="6.5" fill="none" stroke="var(--brand-red)" stroke-width="1.2"/>
        <path d="M4.5,11 H17.5" stroke="var(--brand-red)" stroke-width="1.2"/>
      </svg>
      <span>www.tidalhounds7.net</span>
    </div>
  </div>
</body>
</html>
```